Want to market to schools to offer free chair massages for teacher and staff of the schools

This postcard will be mailed to all public schools in the U.S.

We want the schools to call our company to have a massage therapist provide free chair massages to the teachers and staff at their next School Improvement or Teacher Institute day.

want to make the postcard fun and inviting.

The postcard is 4 1/4" X 6"

FRONT AND BACK DESIGN.

For the back of postcard design, I have attached a template. You can use all the space except where the return label and stamp will go.

Target Market(s)

Target is schools and teachers

Industry/Entity Type

Teacher

```html
<!DOCTYPE html>
<html lang="en">
<head>
<meta charset="utf-8">
<title>BrightPath Wellness – Postcard Back</title>
<link href="https://fonts.googleapis.com/css2?family=Arimo:wght@400&display=swap" rel="stylesheet">
<style>
  :root {
    --paper: #faf6b4;
    --paper-deep: #f6ef86;
    --bleed-line: #e23b3b;
    --safe-line: #5cc56d;
    --fold-line: #1d1d1d;
    --ink-blue: #1a4ec8;
    --ink-sky: #1f86dc;
    --ink-dark: #2a2a2a;
    --mark-navy: #1f2f86;
    --blank: #ffffff;
  }
  * { box-sizing: border-box; margin: 0; padding: 0; }
  html, body { width: 1200px; height: 850px; overflow: hidden; background: #ffffff; }
  body { font-family: "Arimo", Arial, sans-serif; }

  .postcard {
    position: relative;
    width: 1200px;
    height: 850px;
    border: 1px solid var(--bleed-line);
    overflow: hidden;
  }
  .postcard__stripes {
    position: absolute; inset: 0;
    background: linear-gradient(135deg, var(--paper) 0%, var(--paper-deep) 50%, var(--paper) 100%);
  }
  .guide { position: absolute; border: 1px solid var(--safe-line); }
  .guide--trim { left: 23px; top: 23px; right: 23px; bottom: 23px; }
  .guide--safe { left: 46px; top: 44px; width: 1108px; height: 761px; }
  .fold-line {
    position: absolute; left: 0; right: 0; top: 307px;
    border-top: 1px solid var(--fold-line);
  }
  .stamp-box {
    position: absolute; left: 1006px; top: 44px; width: 148px; height: 145px;
    background: var(--blank); border: 1px solid var(--fold-line);
  }

  .brand { position: absolute; left: 63px; top: 60px; display: flex; align-items: center; gap: 10px; }
  .brand__dot { width: 88px; height: 88px; border-radius: 50%; background: var(--mark-navy); flex: none; }
  .brand__name { color: var(--ink-dark); font-size: 33px; line-height: 1.05; font-weight: 400; }

  .contact {
    position: absolute; left: 74px; top: 166px;
    color: var(--ink-blue); font-size: 22px; line-height: 28.5px;
  }

  .testimonial { position: absolute; left: 58px; top: 318px; color: var(--ink-blue); }
  .testimonial__label { font-size: 21px; line-height: 26px; }
  .testimonial__quote { margin: 23px 0 0 5px; width: 330px; font-size: 20.5px; line-height: 27.7px; }
  .testimonial__source {
    width: 282px; text-align: right; margin-top: 8px;
    color: var(--ink-sky); font-size: 20.5px; line-height: 24.5px;
  }

  .photo-slot {
    position: absolute; left: 60px; top: 549px; width: 309px; height: 256px;
    border-radius: 120px 120px 0 0;
    background: linear-gradient(90deg, #8fbfe0 0%, #e8b89a 40%, #d33a3a 65%, #6d3f8e 85%, #f0c6a8 100%);
    opacity: 0.85;
  }

  .address-label {
    position: absolute; left: 408px; top: 425px; width: 600px; height: 286px;
    background: var(--blank);
  }
</style>
</head>
<body>
  <main class="postcard">
    <div class="postcard__stripes" role="img" aria-label="Background of pale yellow diagonal stripes"></div>
    <div class="guide guide--trim"></div>
    <div class="guide guide--safe"></div>
    <div class="fold-line"></div>
    <div class="stamp-box" aria-label="Stamp area"></div>

    <header class="brand">
      <span class="brand__dot"></span>
      <span class="brand__name">BrightPath<br>Wellness Centers</span>
    </header>

    <address class="contact" style="font-style: normal;">
      Contact info:<br>
      BrightPath Wellness<br>
      1-800-555-0142<br>
      www.Brightpathwellness.com
    </address>

    <section class="testimonial">
      <p class="testimonial__label">Testimonial:</p>
      <blockquote class="testimonial__quote">“ Each teacher was delighted to participate and couldn’t believe the difference 10 minutes in a massage chair made”</blockquote>
      <p class="testimonial__source">Marlene<br>Riverside Public School</p>
    </section>

    <div class="photo-slot" role="img" aria-label="Photo of a smiling man and woman giving thumbs up"></div>

    <div class="address-label" aria-label="Return address label area"></div>
  </main>
</body>
</html>
```